Holiday Rental Company Flyer Design (DL not A5)

Note from PixelFolk Administration: The category sizing selected is A5, however the project requires DL sized artwork. Please refer to the DL template link below while the 'Special Requirements' are updated accordingly.

Project Brief:
We need a double sided DL flyer designed for an up market Holiday Rental Company that portrays a personalised approach to property management. These are to be used for letter box drops to homes we're specifically targeting so the design should be modern, complimentary colour palette, uncluttered & visually appealing.

Please Download the DL Template from Quillmark here: http://www.quillmark.com.au/qm/ns/propath/UploadResources.aspx?selectedTab=0?pfid=BFB&pf_id=BFB&xnav=easypath-upload-image#Templates

Target Market(s)

Wealthy Home Owners

Industry/Entity Type

It Company

Font styles to use
Other font styles liked:
• Avant Garde Extra Light & Demi

Colors
33b8a4

Requirements
Must have
• DL Flyer sizes (210mm width x 99mm width, plus 3mm bleed)
• Front: Logo, Main Image & Grab
• Back: Contact Details & Brief Description of our business
• Images: Ideally the main image should be the house with the pool but alternatively a lifestyle images could also be used.
Nice to have
• A creative designer!
Should not have
• Clutter & busy designs

```html
<!DOCTYPE html>
<html lang="en">
<head>
<meta charset="utf-8">
<title>Harbourline Stays – DL Flyer Concept 1</title>
<link href="https://fonts.googleapis.com/css2?family=Didact+Gothic&family=Raleway:wght@200;400;700&display=swap" rel="stylesheet">
<style>
  :root {
    --stage: #ebe9e5;
    --teal: #00b294;
    --ink: #231f20;
    --white: #ffffff;
    --text-dark: #2a2a2a;
    --rule: #bdbdbd;
  }
  * { box-sizing: border-box; margin: 0; padding: 0; }
  html, body { width: 1200px; height: 1000px; overflow: hidden; }
  body {
    background: var(--stage);
    font-family: "Didact Gothic", "Century Gothic", sans-serif;
    color: var(--text-dark);
    position: relative;
  }
  .concept-title {
    position: absolute; left: 0; width: 1125px; top: 38px;
    text-align: center; font-size: 29px; letter-spacing: 0.5px; color: #111;
  }
  .side-label {
    position: absolute; font-size: 26px; color: #111;
    transform: rotate(-90deg); transform-origin: left top;
  }
  .side-label--front { left: 112px; top: 345px; }
  .side-label--back { left: 112px; top: 785px; }

  .flyer { position: absolute; left: 180px; width: 833px; height: 417px; overflow: hidden; }
  .flyer--front { top: 90px; }
  .flyer--back { top: 549px; background: var(--white); border: 1px solid var(--rule); }

  .block { position: absolute; }
  .front-brand { left: 0; top: 0; width: 431px; height: 272px; background: var(--teal); }
  .brand-name {
    position: absolute; left: 0; width: 100%; top: 52px;
    text-align: center; color: var(--white);
    font-family: "Raleway", sans-serif; font-weight: 200;
    font-size: 49px; line-height: 55px; letter-spacing: 5px;
  }
  .brand-dot {
    position: absolute; left: 199px; top: 175px; width: 34px; height: 34px;
    border: 2px solid var(--white); border-radius: 50%;
  }
  .front-tagline {
    left: 0; top: 272px; width: 431px; height: 145px; background: var(--ink);
    color: var(--teal); text-align: center; font-size: 25px; line-height: 32px;
    padding-top: 35px;
  }
  .photo-main {
    left: 431px; top: 0; width: 402px; height: 417px;
    background: linear-gradient(180deg, #1c1a4a 0%, #4a3c66 35%, #b08a5a 62%, #1a6fd8 82%, #0b3a8a 100%);
  }

  .back-intro { left: 0; top: 0; width: 431px; height: 285px; background: var(--teal); color: var(--white); }
  .back-heading { position: absolute; left: 19px; top: 28px; font-size: 26px; }
  .back-lead {
    position: absolute; left: 19px; top: 73px; width: 400px;
    font-size: 15px; line-height: 19px; color: #d8f3ee;
  }
  .back-cta {
    position: absolute; left: 19px; top: 159px; width: 230px;
    font-size: 16px; line-height: 19.5px;
  }
  .photo-bedroom { left: 262px; top: 146px; width: 169px; height: 139px;
    background: linear-gradient(135deg, #e7d6b8 0%, #e8d230 45%, #d9573f 75%, #3c7fb8 100%); }
  .photo-sea { left: 431px; top: 146px; width: 161px; height: 139px;
    background: linear-gradient(160deg, #46c3c8 0%, #2aa9b2 55%, #5a5550 100%); }

  .contact-bar { left: 0; top: 285px; width: 592px; height: 132px; background: var(--ink); color: var(--white); }
  .contact-row { position: absolute; display: flex; align-items: center; gap: 10px; font-size: 16px; }
  .contact-row svg { flex: none; }
  .contact-phone { left: 22px; top: 17px; font-size: 24px; }
  .contact-post { left: 24px; top: 55px; }
  .contact-mail { left: 24px; top: 81px; }
  .contact-web { left: 310px; top: 81px; }

  .service-intro {
    position: absolute; left: 459px; top: 27px; width: 350px;
    font-size: 18px; line-height: 26.5px; color: #3a3a3a;
  }
  .service-intro strong { font-family: "Raleway", sans-serif; font-weight: 700; color: #111; }
  .benefits { position: absolute; left: 607px; top: 141px; width: 215px; list-style: none; }
  .benefit { position: relative; padding-left: 37px; font-size: 15.5px; line-height: 22.5px; color: #222; margin-bottom: 18px; }
  .benefit svg { position: absolute; left: 0; top: 4px; }
</style>
</head>
<body>
  <h1 class="concept-title">CONCEPT 1</h1>
  <div class="side-label side-label--front">FRONT</div>
  <div class="side-label side-label--back">BACK</div>

  <section class="flyer flyer--front">
    <div class="block front-brand">
      <div class="brand-name">HARBOURLINE<br>STAYS</div>
      <div class="brand-dot"></div>
    </div>
    <div class="block front-tagline">Holiday Rental Management<br>with a difference</div>
    <div class="block photo-main" role="img" aria-label="Photo of a modern luxury home at dusk with a lit swimming pool"></div>
  </section>

  <section class="flyer flyer--back">
    <div class="block back-intro">
      <h2 class="back-heading">What we do differently!</h2>
      <p class="back-lead">Rather than relying upon a key safe or a central pick-up destination, a ‘Harbourline Stays’ staff member will greet guests upon arrival.</p>
      <p class="back-cta">If you’d like to know what your property could achieve or require additional information, please contact us on:</p>
    </div>
    <div class="block photo-bedroom" role="img" aria-label="Photo of a bed with yellow cushions and a colourful quilt"></div>
    <div class="block photo-sea" role="img" aria-label="Photo of seals swimming in clear turquoise water"></div>

    <div class="block contact-bar">
      <div class="contact-row contact-phone">
        <svg width="20" height="20" viewBox="0 0 24 24"><path fill="#00b294" d="M6.6 10.8a15 15 0 0 0 6.6 6.6l2.2-2.2a1 1 0 0 1 1-.25 11.4 11.4 0 0 0 3.6.57 1 1 0 0 1 1 1V20a1 1 0 0 1-1 1A17 17 0 0 1 3 4a1 1 0 0 1 1-1h3.5a1 1 0 0 1 1 1c0 1.25.2 2.45.57 3.57a1 1 0 0 1-.25 1z"/></svg>
        <span>(03)5900 4127</span>
      </div>
      <div class="contact-row contact-post">
        <svg width="16" height="16" viewBox="0 0 24 24"><path fill="#00b294" d="M12 2a6 6 0 0 0-6 6c0 4.5 6 10 6 10s6-5.5 6-10a6 6 0 0 0-6-6zm0 8.5A2.5 2.5 0 1 1 12 5.5a2.5 2.5 0 0 1 0 5zM3 20h18v2H3z"/></svg>
        <span>PO Box 18, Kelsey Bay Victoria 3950</span>
      </div>
      <div class="contact-row contact-mail">
        <svg width="16" height="16" viewBox="0 0 24 24"><path fill="#00b294" d="M2 5h20v14H2zm2 2v.5l8 5 8-5V7z"/></svg>
        <span>stay@harbourlinestays.com.au</span>
      </div>
      <div class="contact-row contact-web">
        <svg width="16" height="16" viewBox="0 0 24 24"><circle cx="12" cy="12" r="10" fill="#00b294"/><path fill="none" stroke="#231f20" stroke-width="1.5" d="M2 12h20M12 2c3 3 3 17 0 20M12 2c-3 3-3 17 0 20"/></svg>
        <span>harbourlinestays.com.au</span>
      </div>
    </div>

    <p class="service-intro">Our <strong>‘Meet &amp; Greet’</strong> service provides home owners with an increased level of Security and also allows us to:</p>
    <ul class="benefits">
      <li class="benefit"><svg width="24" height="24" viewBox="0 0 24 24"><circle cx="12" cy="12" r="12" fill="#00b294"/><path d="M6.5 12.5l3.5 3.5 7.5-8" fill="none" stroke="#fff" stroke-width="2.2"/></svg>Prepare the home for their arrival ( lights, heaters, music etc.)</li>
      <li class="benefit"><svg width="24" height="24" viewBox="0 0 24 24"><circle cx="12" cy="12" r="12" fill="#00b294"/><path d="M6.5 12.5l3.5 3.5 7.5-8" fill="none" stroke="#fff" stroke-width="2.2"/></svg>Establish a rapport &amp;help facilitate future bookings</li>
      <li class="benefit"><svg width="24" height="24" viewBox="0 0 24 24"><circle cx="12" cy="12" r="12" fill="#00b294"/><path d="M6.5 12.5l3.5 3.5 7.5-8" fill="none" stroke="#fff" stroke-width="2.2"/></svg>Reiterate their responsibilities to ensure the return of their bond</li>
    </ul>
  </section>
</body>
</html>
```